Letterhead design of KESTREL POWER THRIFT INC.

we are a energy saving company doing the solar screen, radian barrier, attic insulation, double panel windows. Basically i need the design of the letterhead including my company name, business address, phone numbers, fax number and email address. Main thing i need it look like a huge company and look like very high class. thanks !!

Reason: Please send me more new design about my company! Thanks so much!!

Industry/Entity Type

Business

```html
<!DOCTYPE html>
<html lang="en">
<head>
<meta charset="utf-8">
<title>Kestrel Power Thrift Inc. — Letterhead</title>
<link rel="stylesheet" href="https://fonts.googleapis.com/css2?family=Arimo:wght@400;700&display=swap">
<style>
  :root {
    --paper: #ffffff;
    --sky-light: #e6f1f7;
    --sky-mid: #8fcbe0;
    --sky-deep: #00a3c8;
    --leaf: #8dc63f;
    --ink: #111111;
    --brand-blue: #0aa3cb;
    --mark-faint: rgba(40, 150, 195, 0.22);
    --name-faint: rgba(120, 140, 160, 0.45);
    --footer-text: #ffffff;
  }
  html, body {
    margin: 0;
    padding: 0;
    overflow: hidden;
    background: #ffffff;
  }
  .letterhead {
    position: relative;
    width: 928px;
    height: 1200px;
    box-sizing: border-box;
    border: 1px solid var(--ink);
    overflow: hidden;
    font-family: "Arimo", Arial, sans-serif;
    background: linear-gradient(
      to bottom,
      var(--paper) 0px,
      var(--paper) 320px,
      var(--sky-light) 480px,
      var(--sky-mid) 900px,
      #4cb9d6 1080px,
      var(--sky-deep) 1200px
    );
  }
  .brand {
    position: absolute;
    left: 84px;
    top: 58px;
    display: flex;
    align-items: center;
    gap: 10px;
  }
  .brand-square {
    width: 22px;
    height: 22px;
    background: var(--brand-blue);
  }
  .brand-name {
    margin: 0;
    font-size: 22px;
    font-weight: 700;
    line-height: 1.15;
    color: var(--brand-blue);
    letter-spacing: 0.5px;
  }
  .header-band {
    position: absolute;
    left: 241px;
    top: 160px;
    width: 687px;
    height: 28px;
  }
  .watermark-disc {
    position: absolute;
    left: 262px;
    top: 500px;
    width: 390px;
    height: 390px;
    border-radius: 50%;
    background: var(--mark-faint);
  }
  .watermark-name {
    position: absolute;
    left: 0;
    width: 100%;
    top: 1022px;
    margin: 0;
    text-align: center;
    font-size: 40px;
    font-weight: 400;
    color: var(--name-faint);
    letter-spacing: 0.5px;
  }
  .contact {
    position: absolute;
    left: 0;
    width: 100%;
    top: 1092px;
    text-align: center;
    color: var(--footer-text);
    font-weight: 700;
    font-size: 13px;
  }
  .contact p { margin: 0; }
  .contact .email { margin-top: 19px; }
  .contact .sep { color: var(--ink); padding: 0 3px; }
</style>
</head>
<body>
<main class="letterhead">
  <header class="brand">
    <span class="brand-square" aria-hidden="true"></span>
    <h1 class="brand-name">KESTREL POWER<br>THRIFT INC.</h1>
  </header>

  <svg class="header-band" viewBox="0 0 687 28" aria-hidden="true">
    <defs>
      <linearGradient id="bandFill" x1="0" y1="0" x2="1" y2="0">
        <stop offset="0" stop-color="#ffffff"/>
        <stop offset="0.35" stop-color="#8dc63f"/>
        <stop offset="0.55" stop-color="#5bb48a"/>
        <stop offset="0.78" stop-color="#00a3c8"/>
        <stop offset="0.92" stop-color="#111111"/>
        <stop offset="1" stop-color="#000000"/>
      </linearGradient>
    </defs>
    <polygon points="0,12 687,0 687,26 0,28" fill="url(#bandFill)"/>
  </svg>

  <div class="watermark-disc" aria-hidden="true"></div>
  <p class="watermark-name">Kestrel Power Thrift Inc.</p>

  <footer class="contact">
    <p>4180 Brightfield Rd Suite #200 Springvale, Texas 77001<span class="sep">|</span>ph: 555-014-2290<span class="sep">|</span>fax: 555-013-7741</p>
    <p class="email">kestrelpowerthrift@example.com</p>
  </footer>
</main>
</body>
</html>
```